Square Business Cards for Our Restaurant / Event Venue

We need square business cards designed for the management team of our event venue and restaurant. On one side of the card should be the the Harbor Lantern 7 logo and URL www.harborlantern7.example. On the other side should be the Ember Logo and URL www.emberhall7.example. All employee details should be on the side with Ember logo. There will be a total of 5 cards to be created with the design.

Clara Bennquist
clara@harborlantern7.example

main 555.418.3072
direct 555.730.2946

4831 West Orchard Lane SE
Washington, DC 90417

Industry/Entity Type

Business

```html
<!DOCTYPE html>
<html lang="en">
<head>
<meta charset="utf-8">
<title>Harbor Lantern 7 — Business Cards</title>
<link rel="stylesheet" href="https://fonts.googleapis.com/css2?family=Lato:wght@400;700;900&display=swap">
<style>
  :root {
    --stage: #2b2b2b;
    --brand-red: #b52028;
    --card-white: #ffffff;
    --ink: #1a1a1a;
    --ink-soft: #333333;
  }
  * { box-sizing: border-box; margin: 0; padding: 0; }
  html, body { width: 1200px; height: 880px; overflow: hidden; }
  body {
    background: var(--stage);
    font-family: "Lato", Arial, sans-serif;
    position: relative;
  }
  .card {
    position: absolute;
    top: 190px;
    width: 500px;
    height: 500px;
    border-radius: 24px;
    box-shadow: 0 18px 40px rgba(0,0,0,0.45);
    overflow: hidden;
  }

  /* Brand side */
  .card--brand {
    left: 70px;
    background: var(--brand-red);
  }
  .brand-disc {
    position: absolute;
    left: 50%; top: 110px;
    width: 220px; height: 220px;
    margin-left: -110px;
    border-radius: 50%;
    background: var(--card-white);
    display: flex; align-items: center; justify-content: center;
    text-align: center;
  }
  .brand-name {
    color: var(--brand-red);
    font-weight: 700;
    font-size: 30px;
    line-height: 1.15;
  }
  .brand-url {
    position: absolute;
    left: 0; right: 0; top: 372px;
    text-align: center;
    color: var(--card-white);
    font-size: 16px;
    letter-spacing: 0.3px;
  }

  /* Contact side */
  .card--contact {
    left: 630px;
    background: var(--card-white);
  }
  .venue-mark {
    position: absolute;
    left: 34px; top: 190px;
    display: flex; align-items: center; gap: 10px;
  }
  .venue-mark__name {
    font-weight: 900;
    font-size: 54px;
    line-height: 1;
    color: var(--ink);
    letter-spacing: -1px;
  }
  .venue-mark__dot {
    width: 14px; height: 14px; border-radius: 50%;
    background: var(--brand-red);
  }
  .divider {
    position: absolute;
    left: 246px; top: 120px;
    width: 1px; height: 200px;
    background: var(--brand-red);
  }
  .contact {
    position: absolute;
    left: 264px; top: 136px;
    width: 220px;
    color: var(--ink-soft);
  }
  .contact__name {
    font-weight: 700;
    font-size: 19px;
    color: var(--ink);
  }
  .contact__email {
    font-size: 12.5px;
    margin-top: 2px;
    white-space: nowrap;
  }
  .contact__phones {
    list-style: none;
    margin-top: 18px;
  }
  .contact__phones li {
    display: flex; align-items: center; gap: 8px;
    font-size: 16px;
    line-height: 24px;
  }
  .contact__phones svg { width: 16px; height: 16px; flex: none; }
  .contact__web {
    margin-top: 18px;
    font-size: 14px;
  }
  .contact__web span { color: var(--brand-red); }
  .address {
    position: absolute;
    left: 0; right: 0; bottom: 56px;
    text-align: center;
    font-size: 16px;
    color: var(--ink);
  }
</style>
</head>
<body>

  <section class="card card--brand" aria-label="Card front">
    <div class="brand-disc">
      <span class="brand-name">Harbor<br>Lantern 7</span>
    </div>
    <p class="brand-url">www.harborlantern7.example</p>
  </section>

  <section class="card card--contact" aria-label="Card back">
    <div class="venue-mark">
      <span class="venue-mark__name">Ember</span>
      <span class="venue-mark__dot"></span>
    </div>

    <div class="divider"></div>

    <div class="contact">
      <p class="contact__name">Clara Bennquist</p>
      <p class="contact__email">clara@harborlantern7.example</p>
      <ul class="contact__phones">
        <li>
          <svg viewBox="0 0 16 16" aria-hidden="true">
            <circle cx="8" cy="8" r="7.2" fill="none" stroke="#b52028" stroke-width="1.2"/>
            <path d="M5 5.2c.6-.6 1.2-.4 1.5.2l.5 1c.2.4 0 .7-.3 1 .4.9 1 1.5 1.9 1.9.3-.3.6-.5 1-.3l1 .5c.6.3.8.9.2 1.5-2.6 1.6-7.4-3.2-5.8-5.8z" fill="#b52028"/>
          </svg>
          555.418.3072
        </li>
        <li>
          <svg viewBox="0 0 16 16" aria-hidden="true">
            <circle cx="8" cy="8" r="7.2" fill="none" stroke="#b52028" stroke-width="1.2"/>
            <rect x="5.5" y="3.8" width="5" height="8.4" rx="1" fill="none" stroke="#b52028" stroke-width="1.1"/>
            <circle cx="8" cy="10.8" r="0.6" fill="#b52028"/>
          </svg>
          555.730.2946
        </li>
      </ul>
      <p class="contact__web">www.<span>emberhall7</span>.example</p>
    </div>

    <p class="address">4831 West Orchard Lane SE Washington, DC 90417</p>
  </section>

</body>
</html>
```